Website design for learning and development business

I need a logo for my new business based in Australasia. I am a kiwi who is a creative change maker working in the Learning & development space. I design experiential learning opportunities for businesses to grow and nurture their tribes. I take a holistic look at an organisation and analyse what is needed to build a positive culture with a growth mindset woven into their DNA. I would like to see designs that are based on the following word snaps - creative, interesting, tribal, journey, adaptability, engaging, fluid, architectural, bespoke, courageous, challenging .I have the logo (attached) and I Need a startup business website designed. I am a Learning and development professional who is looking at going out on my own and establishing my own business. I would like a website designed that people would go to to check out what I do, how I do, what skills I have and how to contact me. Also room for a blog/articles.

Target Market(s)

Small to medium business

Industry/Entity Type

Self employed training and consultancy company

Number of Pages Required

5+ page

Requirements
Must have
• home page, about page, contact us page, blog page, search for us page
Nice to have
• Testimonials,

```html
<!DOCTYPE html>
<html lang="en">
<head>
<meta charset="utf-8">
<title>Kowhai Consulting – Skills I Have</title>
<link href="https://fonts.googleapis.com/css2?family=Open+Sans:wght@400;600;700&family=Saira:wght@600;700&display=swap" rel="stylesheet">
<style>
  :root{
    --cyan:#00ffff;
    --hero-dark:#1b1616;
    --ink:#1f1f1f;
    --body:#333333;
    --white:#ffffff;
    --footer:#000000;
    --orange:#ef6236;
    --red:#d9141c;
    --navy:#2b2f7d;
    --blue:#3b8bd0;
    --olive:#c5c61a;
    --green:#2a992b;
  }
  *{margin:0;padding:0;box-sizing:border-box}
  html,body{width:1200px;height:3362px;overflow:hidden;background:var(--white)}
  body{position:relative;font-family:"Open Sans",sans-serif;color:var(--body)}
  .abs{position:absolute}

  /* hero */
  .hero{position:absolute;left:0;top:0;width:1200px;height:560px;background:var(--hero-dark);overflow:hidden}
  .hero-photo{position:absolute;left:575px;top:111px;width:330px;height:380px;border-radius:45% 40% 20% 30%;
    background:radial-gradient(ellipse at 55% 40%,#2fa79a 0%,#1f7f78 35%,#3c5a4e 60%,rgba(60,60,60,0) 78%)}
  .hero-wave{position:absolute;left:0;top:0}
  .brand{position:absolute;left:171px;top:82px;display:flex;align-items:center;gap:12px;
    font-family:"Saira",sans-serif;font-weight:700;font-size:30px;letter-spacing:1px;color:var(--white)}
  .brand-dot{width:22px;height:22px;border-radius:50%;background:var(--cyan)}
  .nav{position:absolute;top:54px;height:54px;display:flex;align-items:center}
  .nav a{position:absolute;white-space:nowrap;font-weight:700;font-size:15.5px;color:var(--white);text-decoration:none}
  .nav-cta{position:absolute;left:889px;top:54px;width:137px;height:54px;border-radius:6px;background:var(--cyan);
    color:#0c2b2b;font-weight:700;font-size:15px;display:flex;align-items:center;justify-content:center}
  .hero-title{position:absolute;left:171px;top:252px;font-family:"Saira",sans-serif;font-weight:700;font-size:48px;
    color:var(--white);letter-spacing:-0.5px}

  /* skills */
  .section-title{position:absolute;left:0;top:640px;width:1200px;text-align:center;font-family:"Saira",sans-serif;
    font-weight:700;font-size:37px;color:var(--ink)}
  .skill-tile{position:absolute;width:389px;height:324px}
  .skill-badge{position:absolute;width:70px;height:70px;border-radius:50%;border:3px solid var(--white);
    box-shadow:0 3px 8px rgba(0,0,0,.3);display:flex;align-items:center;justify-content:center}
  .skill-text{position:absolute;width:411px}
  .skill-text h3{font-weight:400;font-size:25px;color:var(--ink);letter-spacing:.3px;margin-bottom:14px}
  .skill-text p{font-size:13.6px;line-height:22.6px;text-align:justify}

  /* footer */
  .footer{position:absolute;left:0;top:2834px;width:1200px;height:528px;background:var(--footer)}
  .footer-title{position:absolute;left:171px;top:2945px;font-family:"Saira",sans-serif;font-weight:700;font-size:28px;color:var(--white)}
  .field{position:absolute;left:172px;width:268px;height:56px;border-radius:10px;background:var(--white);
    font-size:15px;color:#333;padding:0 12px;display:flex;align-items:center}
  .submit{position:absolute;left:172px;top:3137px;width:118px;height:56px;border-radius:8px;background:var(--cyan);
    display:flex;align-items:center;justify-content:center;font-weight:600;font-size:16px;color:#0c2b2b}
  .footer-brand{position:absolute;left:568px;top:3100px;width:460px;display:flex;align-items:center;justify-content:flex-end;gap:16px;
    font-family:"Saira",sans-serif;font-weight:700;font-size:44px;color:var(--white);white-space:nowrap}
  .footer-brand .brand-dot{width:34px;height:34px}
  .footer-rule{position:absolute;left:172px;top:3269px;width:856px;height:1px;background:#555}
  .copyright{position:absolute;left:0;top:3305px;width:1200px;text-align:center;font-weight:600;font-size:13px;color:var(--white)}
</style>
</head>
<body>

<header class="hero">
  <div class="hero-photo" role="img" aria-label="Photo of a green chameleon perched on a hand"></div>
  <svg class="hero-wave" width="1200" height="560" viewBox="0 0 1200 560">
    <path d="M0,448 C70,405 150,372 250,392 C360,414 440,500 580,515 C720,528 820,470 960,488 C1030,497 1070,510 1100,515 L1100,560 L0,560 Z" fill="var(--cyan)"/>
    <path d="M0,512 C120,492 230,470 360,492 C470,512 520,532 600,532 C720,532 860,508 1000,512 C1080,514 1150,500 1185,522 C1195,530 1200,540 1200,545 L1200,560 L0,560 Z" fill="var(--white)"/>
  </svg>
  <div class="brand"><span class="brand-dot"></span>KOWHAI CONSULTING</div>
  <nav class="nav">
    <a style="left:551px">HOME</a>
    <a style="left:619px">ABOUT</a>
    <a style="left:699px">CONTACT US</a>
    <a style="left:825px">BLOG</a>
  </nav>
  <div class="nav-cta">SEARCH FOR US</div>
  <h1 class="hero-title">SKILLS I HAVE</h1>
</header>

<h2 class="section-title">WHAT SKILLS I HAVE</h2>

<!-- Creative -->
<svg class="skill-tile" style="left:172px;top:755px" viewBox="0 0 389 324" role="img" aria-label="Photo of a light bulb pencil drawing a glowing line">
  <defs><linearGradient id="gCreative" x1="0" y1="0" x2="1" y2="1"><stop offset="0" stop-color="#7ea6b8"/><stop offset="1" stop-color="#1d3f5c"/></linearGradient></defs>
  <polygon points="12,12 377,37 377,288 12,312" fill="url(#gCreative)" stroke="url(#gCreative)" stroke-width="24" stroke-linejoin="round"/>
</svg>
<div class="skill-badge" style="left:523px;top:883px;background:var(--orange)">
  <svg width="36" height="36" viewBox="0 0 36 36" fill="none" stroke="#fff" stroke-width="2.2" stroke-linecap="round"><circle cx="18" cy="17" r="8"/><path d="M14 17l3 3 5-6M15 28h6M18 3v3M6 8l2 2M30 8l-2 2M3 17h3M30 17h3"/></svg>
</div>
<div class="skill-text" style="left:618px;top:803px">
  <h3>CREATIVE</h3>
  <p>Nemo enim ipsam voluptatem quia voluptas sit aspernatur aut odit aut fugit, sed quia consequuntur magni dolores eos qui ratione voluptatem sequi nesciunt. Neque porro quisquam est, qui dolorem ipsum quia dolor sit amet, consectetur, adipisci velit sed quia non numquam eius modi tempora incidunt ut labore et dolore magnam aliquam quaerat voluptatem. Ut enim ad minima veniam, quis nostrum exercitationem ullam corporis suscipit laboriosam, nisi ut aliquid ex ea commodi consequatur.</p>
</div>

<!-- Interesting -->
<div class="skill-text" style="left:172px;top:1133px">
  <h3>INTERESTING</h3>
  <p>Nemo enim ipsam voluptatem quia voluptas sit aspernatur aut odit aut fugit, sed quia consequuntur magni dolores eos qui ratione voluptatem sequi nesciunt. Neque porro quisquam est, qui dolorem ipsum quia dolor sit amet, consectetur, adipisci velit sed quia non numquam eius modi tempora incidunt ut labore et dolore magnam aliquam quaerat voluptatem. Ut enim ad minima veniam, quis nostrum exercitationem ullam corporis suscipit laboriosam, nisi ut aliquid ex ea commodi consequatur.</p>
</div>
<svg class="skill-tile" style="left:638px;top:1087px" viewBox="0 0 389 324" role="img" aria-label="Photo of a woman working at a desktop computer in a studio">
  <defs><linearGradient id="gInteresting" x1="0" y1="0" x2="1" y2="1"><stop offset="0" stop-color="#9a8f84"/><stop offset="1" stop-color="#3d3a38"/></linearGradient></defs>
  <polygon points="12,37 377,12 377,312 12,288" fill="url(#gInteresting)" stroke="url(#gInteresting)" stroke-width="24" stroke-linejoin="round"/>
</svg>
<div class="skill-badge" style="left:606px;top:1213px;background:var(--red)">
  <svg width="36" height="36" viewBox="0 0 36 36" fill="none" stroke="#fff" stroke-width="2.2" stroke-linejoin="round"><path d="M5 7h26v18H15l-7 6v-6H5z"/><circle cx="14" cy="15" r="2.5"/><circle cx="22" cy="15" r="2.5"/><path d="M16.5 15c0 3-2 5-4 5.5M24.5 15c0 3-2 5-4 5.5"/></svg>
</div>

<!-- Tribal -->
<svg class="skill-tile" style="left:172px;top:1417px" viewBox="0 0 389 324" role="img" aria-label="Photo of a dancer in a dark flowing dress on a salt flat under a cloudy sky">
  <defs><linearGradient id="gTribal" x1="0" y1="0" x2="0" y2="1"><stop offset="0" stop-color="#2f4f6e"/><stop offset=".5" stop-color="#8fa3b4"/><stop offset="1" stop-color="#e4e1dc"/></linearGradient></defs>
  <polygon points="12,12 377,37 377,288 12,312" fill="url(#gTribal)" stroke="url(#gTribal)" stroke-width="24" stroke-linejoin="round"/>
</svg>
<div class="skill-badge" style="left:523px;top:1543px;background:var(--navy)">
  <svg width="36" height="36" viewBox="0 0 36 36" fill="none" stroke="#fff" stroke-width="2.2" stroke-linecap="round"><circle cx="18" cy="15" r="3.5"/><path d="M12 29v-5a6 6 0 0 1 12 0v5M6 29v-9M6 14l0-7M3 10l3-3 3 3M30 29v-9M30 14V7M27 10l3-3 3 3"/></svg>
</div>
<div class="skill-text" style="left:618px;top:1464px">
  <h3>TRIBAL</h3>
  <p>Nemo enim ipsam voluptatem quia voluptas sit aspernatur aut odit aut fugit, sed quia consequuntur magni dolores eos qui ratione voluptatem sequi nesciunt. Neque porro quisquam est, qui dolorem ipsum quia dolor sit amet, consectetur, adipisci velit sed quia non numquam eius modi tempora incidunt ut labore et dolore magnam aliquam quaerat voluptatem. Ut enim ad minima veniam, quis nostrum exercitationem ullam corporis suscipit laboriosam, nisi ut aliquid ex ea commodi consequatur.</p>
</div>

<!-- Journey -->
<div class="skill-text" style="left:172px;top:1786px">
  <h3>JOURNEY</h3>
  <p>Nemo enim ipsam voluptatem quia voluptas sit aspernatur aut odit aut fugit, sed quia consequuntur magni dolores eos qui ratione voluptatem sequi nesciunt. Neque porro quisquam est, qui dolorem ipsum quia dolor sit amet, consectetur, adipisci velit sed quia non numquam eius modi tempora incidunt ut labore et dolore magnam aliquam quaerat voluptatem. Ut enim ad minima veniam, quis nostrum exercitationem ullam corporis suscipit laboriosam, nisi ut aliquid ex ea commodi consequatur.</p>
</div>
<svg class="skill-tile" style="left:638px;top:1740px" viewBox="0 0 389 324" role="img" aria-label="Close-up photo of an eye framed by colourful face paint">
  <defs><linearGradient id="gJourney" x1="0" y1="0" x2="1" y2="1"><stop offset="0" stop-color="#d9a87f"/><stop offset=".45" stop-color="#1f8a8f"/><stop offset="1" stop-color="#9fae4a"/></linearGradient></defs>
  <polygon points="12,37 377,12 377,312 12,288" fill="url(#gJourney)" stroke="url(#gJourney)" stroke-width="24" stroke-linejoin="round"/>
</svg>
<div class="skill-badge" style="left:606px;top:1865px;background:var(--blue)">
  <svg width="36" height="36" viewBox="0 0 36 36" fill="none" stroke="#fff" stroke-width="2.2" stroke-linecap="round"><path d="M11 19s-6-6-6-10a6 6 0 0 1 12 0c0 4-6 10-6 10z"/><circle cx="11" cy="9" r="2"/><path d="M26 29s-4-4-4-7a4 4 0 0 1 8 0c0 3-4 7-4 7z"/><path d="M11 23c0 4 4 4 7 4" stroke-dasharray="2 3"/></svg>
</div>

<!-- Adaptability -->
<svg class="skill-tile" style="left:172px;top:2062px" viewBox="0 0 389 324" role="img" aria-label="Photo of a wall with hand lettering about getting creativity flowing">
  <defs><linearGradient id="gAdapt" x1="0" y1="0" x2="1" y2="0"><stop offset="0" stop-color="#3e3f52"/><stop offset=".5" stop-color="#a9aad4"/><stop offset="1" stop-color="#55567a"/></linearGradient></defs>
  <polygon points="12,12 377,37 377,288 12,312" fill="url(#gAdapt)" stroke="url(#gAdapt)" stroke-width="24" stroke-linejoin="round"/>
</svg>
<div class="skill-badge" style="left:523px;top:2188px;background:var(--olive)">
  <svg width="36" height="36" viewBox="0 0 36 36" fill="none" stroke="#fff" stroke-width="2.2" stroke-linecap="round" stroke-linejoin="round"><rect x="5" y="7" width="26" height="22" rx="3"/><path d="M11 15h14l-3-3M25 21H11l3 3"/></svg>
</div>
<div class="skill-text" style="left:618px;top:2109px">
  <h3>ADAPTABILITY</h3>
  <p>Nemo enim ipsam voluptatem quia voluptas sit aspernatur aut odit aut fugit, sed quia consequuntur magni dolores eos qui ratione voluptatem sequi nesciunt. Neque porro quisquam est, qui dolorem ipsum quia dolor sit amet, consectetur, adipisci velit sed quia non numquam eius modi tempora incidunt ut labore et dolore magnam aliquam quaerat voluptatem. Ut enim ad minima veniam, quis nostrum exercitationem ullam corporis suscipit laboriosam, nisi ut aliquid ex ea commodi consequatur.</p>
</div>

<!-- Engaging -->
<div class="skill-text" style="left:172px;top:2431px">
  <h3>ENGAGING</h3>
  <p>Nemo enim ipsam voluptatem quia voluptas sit aspernatur aut odit aut fugit, sed quia consequuntur magni dolores eos qui ratione voluptatem sequi nesciunt. Neque porro quisquam est, qui dolorem ipsum quia dolor sit amet, consectetur, adipisci velit sed quia non numquam eius modi tempora incidunt ut labore et dolore magnam aliquam quaerat voluptatem. Ut enim ad minima veniam, quis nostrum exercitationem ullam corporis suscipit laboriosam, nisi ut aliquid ex ea commodi consequatur.</p>
</div>
<svg class="skill-tile" style="left:638px;top:2385px" viewBox="0 0 389 324" role="img" aria-label="Photo of a video editor working at a multi-monitor workstation">
  <defs><linearGradient id="gEngaging" x1="0" y1="0" x2="1" y2="1"><stop offset="0" stop-color="#b8b4ab"/><stop offset=".6" stop-color="#4b4a4c"/><stop offset="1" stop-color="#2b2a2c"/></linearGradient></defs>
  <polygon points="12,37 377,12 377,312 12,288" fill="url(#gEngaging)" stroke="url(#gEngaging)" stroke-width="24" stroke-linejoin="round"/>
</svg>
<div class="skill-badge" style="left:606px;top:2511px;background:var(--green)">
  <svg width="36" height="36" viewBox="0 0 36 36" fill="none" stroke="#fff" stroke-width="2.2" stroke-linecap="round" stroke-linejoin="round"><rect x="5" y="6" width="26" height="18" rx="2"/><rect x="10" y="10" width="16" height="10"/><path d="M13 30h10M18 24v6"/></svg>
</div>

<footer class="footer"></footer>
<h2 class="footer-title">CONTACT US</h2>
<div class="field" style="top:3001px">Name</div>
<div class="field" style="top:3069px">Phone</div>
<div class="submit">SUBMIT</div>
<div class="footer-brand"><span class="brand-dot"></span>KOWHAI CONSULTING</div>
<div class="footer-rule"></div>
<p class="copyright">COPYRIGHTS&nbsp; 2021 KOWHAI.</p>

</body>
</html>
```